Designing the poster for an original Broadway-style musical

We need a poster design for the original children's musical, MOSS LANTERN AND THE MARCHING TINKERS. The had avery successful run and it is now being published. This poster/graphic design will be used for the publication cover as well as the poster for future productions. The design needs to incorporate the title: MOSS LANTERN AND THE MARCHING TINKERS. It must also include: Book by Rob Fallow, Music by Darby Quillen, and Lyrics by Melinda Fallow. It should be a Broadway caliber design.

Target Market(s)

Theatre Producers, Theatre audiences

Industry/Entity Type

Entertainment

Requirements
Must have
• MOSS LANTERN AND THE MARCHING TINKERS
• Book by Rob Fallow, Music by Darby Quillen, Lyrics by Melinda Fallow
Nice to have
• Colorful, bright, energetic.
Should not have
• No Pelham figures. As seen in our photos... our Moss Lantern resembles Pelham's but is our own.

```html
<!DOCTYPE html>
<html lang="en">
<head>
<meta charset="utf-8">
<title>Moss Lantern and the Marching Tinkers — Poster</title>
<link rel="stylesheet" href="https://fonts.googleapis.com/css2?family=Marcellus&family=Kaushan+Script&family=Playfair+Display:ital,wght@1,700&family=Roboto+Condensed:wght@500;700&display=swap">
<style>
  :root {
    --backdrop: #d9dadb;
    --sky-top: #0a5579;
    --sky-mid: #1a6b93;
    --sky-low: #5f9ab8;
    --frost: #cfe4ee;
    --snow: #eaf4f8;
    --glow: rgba(190, 240, 255, 0.75);
    --dancer-tone: rgba(110, 210, 232, 0.6);
    --title-white: #ffffff;
    --credit-ink: #17365a;
  }
  * { margin: 0; padding: 0; box-sizing: border-box; }
  html, body {
    width: 1200px;
    height: 1200px;
    overflow: hidden;
    background: var(--backdrop);
  }
  .canvas {
    position: relative;
    width: 1200px;
    height: 1200px;
  }
  .poster {
    position: absolute;
    left: 239px;
    top: 40px;
    width: 722px;
    height: 1120px;
    overflow: hidden;
  }
  .poster__scene {
    position: absolute;
    inset: 0;
    background:
      radial-gradient(circle at 50% 12%, var(--glow) 0%, rgba(150, 225, 245, 0.25) 9%, rgba(150, 225, 245, 0) 24%),
      radial-gradient(ellipse 70% 18% at 50% 20%, rgba(120, 200, 230, 0.35) 0%, rgba(120, 200, 230, 0) 100%),
      radial-gradient(ellipse 90% 12% at 50% 66%, rgba(140, 205, 230, 0.25) 0%, rgba(140, 205, 230, 0) 100%),
      linear-gradient(180deg,
        var(--sky-top) 0%,
        var(--sky-mid) 38%,
        var(--sky-mid) 55%,
        var(--sky-low) 76%,
        var(--frost) 86%,
        var(--snow) 100%);
  }
  .poster__dancer {
    position: absolute;
    left: 210px;
    top: 78px;
    width: 300px;
    height: 370px;
    border-radius: 46% 46% 40% 40%;
    background: radial-gradient(ellipse at 50% 38%,
      var(--dancer-tone) 0%,
      rgba(90, 195, 225, 0.35) 40%,
      rgba(90, 195, 225, 0) 72%);
  }
  .poster__title {
    position: absolute;
    left: 0;
    top: 0;
    width: 722px;
    height: 1120px;
  }
  .title__caps {
    font-family: "Marcellus", serif;
    fill: var(--title-white);
  }
  .title__script {
    font-family: "Kaushan Script", cursive;
    fill: var(--title-white);
  }
  .title__amp {
    font-family: "Playfair Display", serif;
    font-style: italic;
    font-weight: 700;
    fill: var(--title-white);
  }
  .poster__credits {
    position: absolute;
    left: 0;
    right: 0;
    top: 1004px;
    text-align: center;
    color: var(--credit-ink);
    font-family: "Roboto Condensed", sans-serif;
  }
  .credits__book {
    font-weight: 700;
    font-size: 25px;
    letter-spacing: 0.32em;
    line-height: 1;
  }
  .credits__team {
    margin-top: 8px;
    font-weight: 500;
    font-size: 12.5px;
    letter-spacing: 0.01em;
    line-height: 1;
  }
</style>
</head>
<body>
<div class="canvas">
  <section class="poster">
    <div class="poster__scene" role="img" aria-label="Deep blue night sky filled with falling snow and soft bokeh lights, fading to a snowy white ground"></div>
    <div class="poster__dancer" role="img" aria-label="Glowing translucent silhouette of a ballerina leaping beneath a burst of light"></div>

    <svg class="poster__title" viewBox="0 0 722 1120" aria-label="Moss Lantern and the Marching Tinkers">
      <text class="title__caps" x="80" y="462" font-size="200" textLength="572" lengthAdjust="spacingAndGlyphs">MOSS</text>
      <text class="title__script" x="172" y="558" font-size="92" textLength="270" lengthAdjust="spacingAndGlyphs">lantern</text>
      <text class="title__amp" x="450" y="650" font-size="220">&amp;</text>
      <text class="title__script" x="238" y="666" font-size="100">The</text>
      <text class="title__script" x="136" y="744" font-size="100" textLength="420" lengthAdjust="spacingAndGlyphs">Marching</text>
      <text class="title__script" x="280" y="876" font-size="132" textLength="392" lengthAdjust="spacingAndGlyphs">Tinkers</text>
    </svg>

    <div class="poster__credits">
      <p class="credits__book">BOOK BY ROB FALLOW</p>
      <p class="credits__team">MUSIC BY DARBY QUILLEN &nbsp;|&nbsp; LYRICS BY MELINDA FALLOW.</p>
    </div>
  </section>
</div>
</body>
</html>
```